Industry / Entity Type

Financial consultancy / advisers

Current site is: http://www.brookvale-partners.com

Looking for a complete overhaul of this site, we are after a clean modern look. Will require the ability to easily add, update and remove content, hence the WordPress design.
Example:
Add case studies
Industry documentation (downloadable brochures / flyers and such)

What we like from our current site is the colour the fonts and the logo (the city of London) we would like to have other city outlines (NYC and Tokyo, Hong Kong, Singapore).

The site will be used by our potential clients to get in contact and re-view the case studies, if possible would like to have a client login area where they can download our documents like NDA’s etc and T&C’s.

Task Outline

Create a Web Design (Coded - Design and coding required)
Designer must provide full implementation/coding depending on the platform chosen by the client (i.e. WordPress theme, HTML/CSS, bootstrap etc.)

Task Description

I need a full website built that must work on desktop and mobile. I can provide the London city skyline and the font file, which we have used. Some stock industrial photos will be required.

Requirements:

*Splash page
*What We Do
*How We do it
*Who Are We? To have the same information and links as the current site
*Why use us?
*Clients: To have the same information and links as the current site
*Partners: To have the same information and links as the current site
*Contact:

Target Market(s)

Financial institutions trading Equities, Futures, Options, Forex and Fixed Income.
Regulators, Exchanges, ECN’s
Buy side firms and Sell side firms

Industry/Entity Type

Financial

Coding

Coded - Design and coding required

Number of Pages Required

5+ page

Font styles to use
Sans Serif

Colors
f04a50

Requirements
Must have
• Splash page
• What We Do
• How We do it
• Who Are We? To have the same information and links as the current site
• Why use us?
• Clients: To have the same information and links as the current site
• Partners: To have the same information and links as the current site
• Contact:

```html
<!DOCTYPE html>
<html lang="en">
<head>
<meta charset="utf-8">
<title>Brookvale Partners – Financial Consulting Firm</title>
<link rel="stylesheet" href="https://fonts.googleapis.com/css2?family=Carlito:wght@400;700&family=Questrial&family=Michroma&family=Montserrat:wght@700&display=swap">
<style>
:root{
  --brand:#f04a50;
  --ink:#333333;
  --muted:#707070;
  --soft:#f6f6f6;
  --white:#ffffff;
  --hero-dark:#2b2a2c;
  --hero-warm:#a88a5c;
}
*{box-sizing:border-box;margin:0;padding:0}
html,body{width:668px;height:1200px;overflow:hidden;background:var(--white)}
body{position:relative;font-family:"Carlito",Calibri,sans-serif;color:var(--muted)}
.caps{font-family:"Questrial",sans-serif;font-variant:small-caps;letter-spacing:.3px}

/* header */
.site-header{position:absolute;top:0;left:0;width:668px;height:58px;background:var(--white)}
.brand{position:absolute;left:56px;top:17px;display:flex;align-items:center;gap:6px;color:var(--brand);font-family:"Questrial",sans-serif;font-size:13px;letter-spacing:1px}
.brand-dot{width:9px;height:9px;border-radius:50%;background:var(--brand)}
.main-nav{position:absolute;top:31px;left:245px;display:flex;gap:12px;font-size:7px;text-transform:uppercase;font-family:"Questrial",sans-serif;color:var(--ink);letter-spacing:.2px}
.main-nav .active{color:var(--brand);border-bottom:1px solid var(--brand);padding-bottom:4px}

/* hero */
.hero{position:absolute;top:58px;left:0;width:668px;height:332px;background:linear-gradient(180deg,#5d6470 0%,var(--hero-warm) 45%,#3a3430 70%,var(--hero-dark) 100%)}
.hero-title{position:absolute;top:108px;width:100%;text-align:center;font-family:"Michroma",sans-serif;font-size:21px;letter-spacing:3px;color:transparent;-webkit-text-stroke:1px var(--white);text-transform:uppercase}
.slider-dots{position:absolute;top:267px;left:313px;display:flex;gap:3px}
.slider-dots span{width:9px;height:9px;border-radius:50%;background:var(--white)}
.slider-dots span:first-child{background:transparent;border:1px solid var(--white)}
.hero-curve{position:absolute;top:350px;left:0}

/* welcome */
.welcome{position:absolute;top:412px;left:0;width:668px;text-align:center}
.welcome h1{font-family:"Montserrat",sans-serif;font-size:17px;color:var(--ink);letter-spacing:.3px}
.welcome p{width:520px;margin:10px auto 0;font-size:6.6px;line-height:11px}

.services{position:absolute;top:500px;left:56px;width:560px;display:grid;grid-template-columns:196px 193px 171px;row-gap:58px}
.service{display:flex;gap:8px}
.service svg{flex:none;width:30px;height:30px}
.service h3{font-size:10.5px;color:var(--ink);font-weight:700;margin-top:5px}
.service p{font-size:7px;line-height:13.5px;margin-top:5px;width:135px}

/* about */
.about{position:absolute;top:693px;left:0;width:668px;height:293px;background:var(--soft)}
.about h2{position:absolute;left:56px;top:35px;font-size:20px;color:var(--brand)}
.about .lead{position:absolute;left:56px;top:65px;width:300px;font-size:9px;line-height:14px;color:var(--ink)}
.about .body{position:absolute;left:56px;top:103px;width:275px;font-size:6.6px;line-height:13.5px}
.about .body p+p{margin-top:3px}
.btn{position:absolute;left:56px;top:223px;width:82px;height:26px;background:var(--brand);color:var(--white);font-size:11px;display:flex;align-items:center;justify-content:center}
.about-photo{position:absolute;left:372px;top:39px;width:241px;height:203px;border:2px solid var(--white);box-shadow:0 0 3px rgba(0,0,0,.15);background:linear-gradient(135deg,#e9edf2 0%,#c8ccd2 45%,#3c4658 80%,#2a3244 100%)}

/* footer */
.site-footer{position:absolute;top:986px;left:0;width:668px;height:167px;background:var(--brand);color:var(--white)}
.site-footer h4{font-size:14px;letter-spacing:.5px}
.col{position:absolute;top:24px}
.col-links{left:55px}
.col-contact{left:266px}
.col-news{left:439px}
.divider{position:absolute;top:22px;width:1px;height:110px;background:rgba(255,255,255,.2)}
.quick-links{display:grid;grid-template-columns:100px 80px;row-gap:4px;margin-top:12px;font-size:7.5px;list-style:none}
.address{margin-top:9px;font-size:7.5px;line-height:14px}
.contact-line{display:flex;align-items:center;gap:6px;font-size:7.5px;margin-top:6px}
.subscribe{margin-top:10px;width:175px;height:24px;background:var(--white);display:flex;align-items:center;justify-content:space-between;padding:0 4px 0 7px;font-size:6.5px;color:#9a9a9a;text-transform:uppercase}
.subscribe span:last-child{background:var(--brand);color:var(--white);padding:4px 5px;font-weight:700}
.social{display:flex;gap:6px;margin-top:10px;list-style:none}
.social li{width:20px;height:20px;border-radius:50%;background:var(--white)}

.copyright{position:absolute;top:1171px;width:668px;text-align:center;font-size:6.5px;color:#555}
</style>
</head>
<body>

<header class="site-header">
  <div class="brand"><span class="brand-dot"></span>BROOKVALE PARTNERS</div>
  <nav class="main-nav">
    <span class="active">Home</span><span>What we do</span><span>How we do it</span><span>Who are we</span><span>Why use us</span><span>Clients</span><span>Partners</span><span>Contact</span>
  </nav>
</header>

<section class="hero" role="img" aria-label="Business people silhouetted in a glass office hall against a city skyline at sunset">
  <h2 class="hero-title">Financial Consulting Firm</h2>
  <div class="slider-dots"><span></span><span></span><span></span><span></span></div>
</section>
<svg class="hero-curve" width="668" height="42" viewBox="0 0 668 42" aria-hidden="true">
  <path d="M0 40 Q334 -6 668 40 L668 42 L0 42 Z" fill="#ffffff"/>
</svg>

<section class="welcome">
  <h1>WELCOME TO BROOKVALE PARTNERS</h1>
  <p>Since founding Brookvale Partners in 2014 we have dedicated ourselves to the provision of services. What differentiates us from other advisers or consultancies is a genuine motivation to see our clients succeed. Today's technology allows our clients to take their knowledge to the market in ways that previous generations could only dream of. That's why Brookvale is dedicated to seeing you choose the right technology strategy, ensuring you maintain a competitive edge over your peers.</p>
</section>

<section class="services">
  <div class="service">
    <svg viewBox="0 0 30 30"><g fill="#f04a50"><circle cx="7" cy="6" r="3"/><rect x="4" y="10" width="6" height="10"/><rect x="4" y="20" width="2.5" height="9"/><rect x="7.5" y="20" width="2.5" height="9"/></g><rect x="13" y="3" width="15" height="11" fill="none" stroke="#f04a50" stroke-width="1.5"/><line x1="10" y1="12" x2="14" y2="9" stroke="#f04a50" stroke-width="1.5"/></svg>
    <div><h3 class="caps">Training</h3><p>Trading Technology for Compliance and non technical staff.</p></div>
  </div>
  <div class="service">
    <svg viewBox="0 0 30 30"><g fill="#f04a50"><ellipse cx="14" cy="19" rx="11" ry="8"/><rect x="7" y="24" width="3" height="5"/><rect x="17" y="24" width="3" height="5"/><circle cx="21" cy="6" r="5"/></g><text x="21" y="9" font-size="7" fill="#fff" text-anchor="middle" font-family="sans-serif">$</text></svg>
    <div><h3 class="caps">Advice</h3><p>Board Level advisory &amp; Programe Management.</p></div>
  </div>
  <div class="service">
    <svg viewBox="0 0 30 30"><rect x="3" y="5" width="24" height="15" fill="none" stroke="#f04a50" stroke-width="1.5"/><line x1="0" y1="22" x2="30" y2="22" stroke="#f04a50" stroke-width="2"/><polyline points="6,16 11,10 15,14 19,8 24,13" fill="none" stroke="#f04a50" stroke-width="1.5"/></svg>
    <div><h3 class="caps">Product Development</h3><p>Front-Office Trading platforms and Market Data.</p></div>
  </div>
  <div class="service">
    <svg viewBox="0 0 30 30"><path d="M2 11 L15 3 L28 11 V28 H2 Z" fill="#f04a50"/><rect x="7" y="14" width="16" height="12" fill="#fff"/><g fill="#f04a50"><rect x="9" y="16" width="5" height="4"/><rect x="16" y="16" width="5" height="4"/><rect x="9" y="21" width="5" height="4"/><rect x="16" y="21" width="5" height="4"/></g></svg>
    <div><h3 class="caps">Interim Management</h3><p>For Funds, Broker, Vendors and IT Service Providers.</p></div>
  </div>
  <div class="service">
    <svg viewBox="0 0 30 30"><circle cx="12" cy="18" r="8" fill="none" stroke="#f04a50" stroke-width="4" stroke-dasharray="3 2"/><circle cx="12" cy="18" r="3" fill="#f04a50"/><circle cx="24" cy="6" r="4" fill="none" stroke="#f04a50" stroke-width="2.5" stroke-dasharray="2 1.5"/></svg>
    <div><h3 class="caps">Process Outsourcing</h3><p>RFI, RFP &amp; Independent tender evaluations (assess before you invest)</p></div>
  </div>
  <div class="service">
    <svg viewBox="0 0 30 30"><circle cx="15" cy="14" r="7" fill="#f04a50"/><rect x="12" y="21" width="6" height="5" fill="#f04a50"/><g stroke="#f04a50" stroke-width="1.5"><line x1="15" y1="1" x2="15" y2="4"/><line x1="3" y1="14" x2="6" y2="14"/><line x1="24" y1="14" x2="27" y2="14"/><line x1="6" y1="5" x2="8" y2="7"/><line x1="24" y1="5" x2="22" y2="7"/></g></svg>
    <div><h3 class="caps">Research</h3><p>Topical Paper White labelled and sponsered articles.</p></div>
  </div>
</section>

<section class="about">
  <h2 class="caps">About Us</h2>
  <p class="lead">Since founding Brookvale Partners in 2014 we have dedicated ourselves to the provision of services</p>
  <div class="body">
    <p>Since founding Brookvale Partners in 2014 we have dedicated ourselves to the provision of services. What differentiates us from other advisers or consultancies is a genuine motivation to see our clients succeed. Today's technology allows our clients to take their knowledge to the market in ways that previous generations could only dream of.</p>
    <p>Brookvale is dedicated to seeing you choose the right technology strategy, ensuring you maintain a competitive edge over your peers.</p>
  </div>
  <div class="btn caps">Read More »</div>
  <div class="about-photo" role="img" aria-label="Two businessmen reviewing documents on a tablet in a bright office"></div>
</section>

<footer class="site-footer">
  <div class="col col-links">
    <h4 class="caps">Quick Links</h4>
    <ul class="quick-links">
      <li>Home</li><li>Why use us</li><li>What we do</li><li>Clients</li><li>How we do it</li><li>Partners</li><li>Who are we</li><li>Contact</li>
    </ul>
  </div>
  <div class="divider" style="left:234px"></div>
  <div class="col col-contact">
    <h4 class="caps">Contact Us</h4>
    <p class="address">Suite 4 Harlow Court, Eastfield,<br>Northbridge, NB7 2QL</p>
    <div class="contact-line"><svg width="9" height="9" viewBox="0 0 10 10"><path d="M2 0 L4 3 L3 4 Q4 6 6 7 L7 6 L10 8 L8 10 Q3 9 0 2 Z" fill="#fff"/></svg>+11 01 04817263</div>
    <div class="contact-line"><svg width="9" height="8" viewBox="0 0 10 8"><rect width="10" height="8" fill="#fff"/><polyline points="0,0 5,4 10,0" fill="none" stroke="#f04a50"/></svg>admin@brookvale-partners.com</div>
  </div>
  <div class="divider" style="left:416px"></div>
  <div class="col col-news">
    <h4 class="caps">Join Newsletters</h4>
    <div class="subscribe"><span>Email address</span><span>Subscribe</span></div>
    <ul class="social" aria-label="Social channels">
      <li aria-label="Social link"></li><li aria-label="Social link"></li><li aria-label="Social link"></li><li aria-label="Social link"></li><li aria-label="Social link"></li>
    </ul>
  </div>
</footer>

<p class="copyright">© 2017 Brookvale Partners. All right reserved. Term of Use</p>

</body>
</html>
```